1-3 PAGE WEBSITE LANDING PAGE DESIGN FOR REELPITCH.NET

I NEED A DESIGNER THAT HAS A GOOD UNDERSTANDING OF BUSINESS AND MARKETING SO HE CAN TAKE MY SALES SCRIPT AND CONVERT IT INTO A BEAUTIFUL IMAGE AND VIDEO FILLED WEBSITE THAT EXPLAINS EACH POINT BEAUTIFULLY. THE WEBSITE SHOULD BE EASY TO READ AND UNDERSTAND AND NAVIGATE.

PLEASE INCLUDE A EXAMPLES SECTION THAT CAN BE FILTERED BY INDUSTRY.

UNDER EVERY SECTION ON THE WEBSITE WE NEED TO HAVE A CALL TO ACTION BUTTON THAT WILL POP UP INTO A LEAD GEN FORM. THE BUTTON WILL SAY "SIGN UP FOR A FREE VIDEO AD MOCK UP FOR YOUR BUSINESS. No Purchase Necessary."

PLEASE SEE ATTACHED FILES FOR WORD DOC OF CONTENT AND LOGO FOR REELPITCH.NET

Target Market(s)

ALL BUSINESSES WHO WILL BE USING VIDEO ADVERTISEMENT AS PART OF THEIR OVERALL MARKETING STRATEGY FOR YEARS TO COME

Industry/Entity Type

Digital Marketing

Number of Pages Required

2 page

Colors

Designer to choose colors to be used in the design.

Requirements
Must have
• I would like color theme to coordinate with logo color theme
Nice to have
• must include all content included in word document

```html
<!DOCTYPE html>
<html lang="en">
<head>
<meta charset="utf-8">
<title>ReelPitch.net – Make a Promo Video</title>
<link href="https://fonts.googleapis.com/css2?family=Montserrat:wght@400;600;700;800&family=Open+Sans:wght@400;600;700&display=swap" rel="stylesheet">
<style>
:root{
  --yellow:#f3d320;
  --ink:#1d1d1d;
  --dark:#2c2c2c;
  --darker:#1f1f1f;
  --text:#444;
  --muted:#8a8a8a;
  --sky:#cfe5f4;
  --sky-2:#a9cfea;
  --pale:#eef5fb;
  --grey:#efefef;
  --line:#dcdcdc;
  --white:#fff;
  --brand:#2a7fc1;
}
*{box-sizing:border-box;margin:0;padding:0}
html,body{width:1200px;height:4240px;overflow:hidden}
body{font-family:"Open Sans",Arial,sans-serif;color:var(--text);background:var(--white);font-size:15px}
a{text-decoration:none}
h1,h2,h3,h4,.btn,.nav a,.tabs span{font-family:"Montserrat",Arial,sans-serif}
.btn{display:inline-block;background:var(--ink);color:var(--white);font-weight:700;font-size:15px;letter-spacing:1px;padding:18px 40px;text-transform:uppercase}
.btn-outline{background:var(--white);color:var(--ink);border:2px solid var(--ink);font-size:13px;padding:14px 26px;letter-spacing:.5px;text-transform:none;font-weight:600}
.ph{position:relative;display:block}
.play{position:absolute;left:50%;top:50%;width:64px;height:44px;margin:-22px 0 0 -32px;background:var(--ink);border-radius:6px}
.play:after{content:"";position:absolute;left:26px;top:12px;border-left:16px solid var(--white);border-top:10px solid transparent;border-bottom:10px solid transparent}

/* top bar + header */
.topbar{height:32px;background:var(--darker);color:#cfcfcf;font-size:12px;line-height:32px;padding-left:48px;letter-spacing:.3px}
.header{height:56px;display:flex;align-items:center;justify-content:space-between;padding:0 48px;border-bottom:1px solid var(--line)}
.logo{font-family:"Montserrat",Arial,sans-serif;font-weight:800;font-size:24px;color:var(--brand);display:flex;align-items:center;gap:8px}
.logo i{width:14px;height:14px;background:var(--yellow);display:block}
.nav{display:flex;gap:30px}
.nav a{font-size:13px;font-weight:600;color:var(--ink);letter-spacing:.5px}

/* hero */
.hero{height:652px;background:linear-gradient(180deg,#e6f2fb 0%,var(--sky) 55%,var(--sky-2) 100%);text-align:center;position:relative;overflow:hidden}
.hero h1{padding-top:56px;font-size:38px;font-weight:800;color:var(--ink);letter-spacing:1.5px}
.hero p{margin-top:14px;font-size:16px;color:#333}
.hero .btn{margin-top:30px}
.hero-art{position:absolute;left:0;right:0;bottom:0;height:400px;background:linear-gradient(180deg,rgba(169,207,234,0) 0%,#8fb6d6 40%,#6f97ba 70%,#e6a55c 100%)}

/* clients */
.clients{height:172px;display:flex;align-items:center;justify-content:space-between;padding:0 60px;margin-top:20px}
.client{width:230px;height:84px;background:#eef2f6;display:flex;align-items:center;justify-content:center;font-weight:600;font-size:18px;color:#6c7a88}

/* start here */
.start{height:628px;background:var(--dark);color:var(--white);text-align:center;padding-top:58px}
.start h2{font-size:30px;font-weight:600;letter-spacing:1px;line-height:1.25}
.start p{margin:22px auto 0;width:840px;font-size:15px;color:#ddd;line-height:1.7}
.choices{display:flex;justify-content:space-between;padding:0 52px;margin-top:38px}
.choice{width:328px;text-align:left}
.choice .ph{height:172px;border:4px solid var(--yellow)}
.choice .ph.a{background:linear-gradient(135deg,#8a7a6a,#3e4a3f)}
.choice .ph.b{background:linear-gradient(135deg,#4a5560,#23292f)}
.choice .ph.c{background:linear-gradient(135deg,#7d5a4a,#3a3f46)}
.choice h4{text-align:center;font-size:14px;font-weight:700;margin-top:16px;letter-spacing:.5px}
.choice small{display:block;font-size:11px;color:#cfcfcf;margin-top:6px;line-height:1.5}
.select{margin-top:16px;height:46px;background:var(--white);color:#555;font-size:13px;display:flex;align-items:center;justify-content:space-between;padding:0 16px}
.select b{border-top:7px solid #555;border-left:6px solid transparent;border-right:6px solid transparent}

/* features */
.features{height:620px;padding:0 48px}
.feature{display:flex;align-items:center;justify-content:space-between;height:310px}
.feature .copy{width:500px}
.feature h3{font-size:23px;font-weight:600;color:var(--ink)}
.feature p{margin:16px 0 28px;line-height:1.75;font-size:15px;color:var(--muted)}
.feature .ph{width:560px;height:270px;background:linear-gradient(135deg,#e9eefc 0%,#c9d4f6 55%,#4f6fd8 100%)}
.feature .ph.alt{background:linear-gradient(135deg,#3b4a66 0%,#6a5a7e 55%,#d44a6a 100%)}

/* templates */
.templates{height:860px;background:var(--grey);margin-top:60px;text-align:center;padding-top:46px}
.templates h2{font-size:28px;font-weight:700;color:var(--ink);letter-spacing:1px}
.tabs{display:flex;justify-content:center;gap:40px;margin-top:36px}
.tabs span{font-size:14px;font-weight:600;color:#333;letter-spacing:.5px}
.cards{display:flex;justify-content:center;gap:60px;margin-top:44px}
.card{width:320px;height:510px}
.card.purple{background:linear-gradient(180deg,#7b3fd0,#5a23ad)}
.card.green{background:linear-gradient(180deg,#1e8fa6 0%,#53b87a 60%,#f1c9a8 100%)}
.card.photo{background:linear-gradient(180deg,#dfe8ef 0%,#b7a894 55%,#5b6f84 100%)}
.templates .btn-outline{margin-top:40px}

/* reviews */
.reviews{height:600px;padding-top:60px;text-align:center}
.reviews h2{font-size:28px;font-weight:600;color:var(--ink);letter-spacing:1px}
.review-row{display:flex;justify-content:space-between;padding:0 88px;margin-top:44px}
.review{width:300px;text-align:left}
.avatar{width:180px;height:180px;border-radius:50%;margin:0 auto;background:linear-gradient(180deg,#f2efe9,#c9b9a6 60%,#4b4f57)}
.review q{display:block;margin-top:40px;font-size:14px;line-height:1.6;color:#555;quotes:"\201C" "\201D"}
.review b{display:block;margin-top:10px;font-size:14px;color:var(--ink)}
.review small{display:block;margin-top:20px;font-size:13px;color:var(--muted)}

/* cta */
.cta{height:220px;background:var(--pale);text-align:center;padding-top:58px}
.cta h2{font-size:28px;font-weight:400;color:#3e77a8}
.cta .btn{margin-top:26px;background:var(--white);color:var(--ink);border:4px solid var(--yellow);padding:14px 40px;font-size:15px}

/* footer */
.footer{height:228px;padding:36px 48px 0;display:flex;justify-content:space-between}
.footer .logo{font-size:22px}
.socials{display:flex;gap:10px;margin-top:20px}
.socials i{width:22px;height:22px;border-radius:50%;background:#3b3b3b;display:block}
.col h4{font-size:14px;font-weight:700;color:var(--ink);margin-bottom:12px}
.col a{display:block;font-size:12px;color:#666;line-height:1.9}
.copyright{height:52px;background:var(--darker);color:#ccc;text-align:center;line-height:52px;font-size:12px}
</style>
</head>
<body>

<div class="topbar">CALL US ON: UK: +44 20 7946 0321 | USA: +1 555 014 2290</div>
<header class="header">
  <div class="logo"><i></i>REELPITCH.NET</div>
  <nav class="nav">
    <a href="#">HOME</a><a href="#">TEMPLATES</a><a href="#">EXAMPLES ▾</a><a href="#">PRODUCT</a><a href="#">PRICING</a><a href="#">LOGIN</a><a href="#">SIGNUP</a>
  </nav>
</header>

<section class="hero">
  <h1>MAKE A PROMO VIDEO FOR YOUR COMPANY</h1>
  <p>People love video. We know that animation isn't easy, but it's a must if you want to captivate your audience.</p>
  <a class="btn" href="#">Start your 7-days trial</a>
  <div class="hero-art ph" role="img" aria-label="Illustration of a blue city skyline with a presenter pointing at a screen showing an animated cat and a play button"><span class="play"></span></div>
</section>

<section class="clients">
  <div class="client">Brightmart</div>
  <div class="client">Deckhouse Studio</div>
  <div class="client">Velocell</div>
  <div class="client">Lakeshore University</div>
</section>

<section class="start">
  <h2>START HERE:<br>WHAT TYPE OF VIDEO WOULD YOU LIKE TO CREATE?</h2>
  <p>Choose the type of video you would like to create, your video use case or the industry you operate in. We'll then take you to a page with examples that are relevant to your needs.</p>
  <div class="choices">
    <div class="choice">
      <div class="ph a" role="img" aria-label="Photo of a person filming a video"><span class="play"></span></div>
      <h4>VIDEO TYPE</h4>
      <small>Select the type of video you would like to create from the drop down menu below.</small>
      <div class="select">Select Video Type <b></b></div>
    </div>
    <div class="choice">
      <div class="ph b" role="img" aria-label="Photo of a team meeting around a table"><span class="play"></span></div>
      <h4>VIDEO USE CASE</h4>
      <small>Select the use case of your video from the drop down menu below.</small>
      <div class="select">Select Use Case <b></b></div>
    </div>
    <div class="choice">
      <div class="ph c" role="img" aria-label="Photo of a shop counter representing an industry"><span class="play"></span></div>
      <h4>YOUR INDUSTRY</h4>
      <small>Select the industry you operate in from the drop down menu below.</small>
      <div class="select">Select Industry <b></b></div>
    </div>
  </div>
</section>

<section class="features">
  <div class="feature">
    <div class="copy">
      <h3>Create Marketing Videos Easily</h3>
      <p>Lorem Ipsum is simply dummy text of the printing and typesetting industry. Lorem Ipsum has been the industry's standard dummy text ever since the 1500s.</p>
      <a class="btn btn-outline" href="#">Create Marketing Videos</a>
    </div>
    <div class="ph" role="img" aria-label="Screenshot of the video editor with an animated character"><span class="play"></span></div>
  </div>
  <div class="feature">
    <div class="ph alt" role="img" aria-label="Screenshot of the editor with a sale promo template"><span class="play"></span></div>
    <div class="copy">
      <h3>Professional results in just a few minutes</h3>
      <p>Lorem Ipsum is simply dummy text of the printing and typesetting industry. Lorem Ipsum has been the industry's standard dummy text ever since the 1500s.</p>
      <a class="btn btn-outline" href="#">Create Professional Videos</a>
    </div>
  </div>
</section>

<section class="templates">
  <h2>MOST POPULAR PROMOTIONAL VIDEO TEMPLATES</h2>
  <div class="tabs"><span>BUSINESS</span><span>PRODUCT PRESENTATION</span><span>MARKETING</span><span>E-COMMERCE</span><span>PROMOTIONAL VIDEO</span><span>STARTUP</span><span>TUTORIAL</span></div>
  <div class="cards">
    <div class="card purple ph" role="img" aria-label="Template preview: illustrated phone with a new badge on purple"><span class="play"></span></div>
    <div class="card green ph" role="img" aria-label="Template preview: hand holding a green phone with title text"><span class="play"></span></div>
    <div class="card photo ph" role="img" aria-label="Template preview: photo of a person outdoors with caption"><span class="play"></span></div>
  </div>
  <a class="btn btn-outline" href="#">View All Templates</a>
</section>

<section class="reviews">
  <h2>CLIENTS REVIEWS</h2>
  <div class="review-row">
    <div class="review">
      <div class="avatar" role="img" aria-label="Portrait photo of a client"></div>
      <q>Using ReelPitch, we achieved a 12x ROI after just a few days. Our clients are so happy about the added value of video.</q>
      <b>Lorem Ipsum Dummy Text</b>
      <small>Regional Director LOREM IPSUM</small>
    </div>
    <div class="review">
      <div class="avatar" role="img" aria-label="Portrait photo of a client"></div>
      <q>Video content has helped increase our email marketing click-through rates by engaging animated videos.</q>
      <b>Lorem Ipsum Dummy Text</b>
      <small>Digital Manager LOREM IPSUM</small>
    </div>
    <div class="review">
      <div class="avatar" role="img" aria-label="Portrait photo of a client"></div>
      <q>We increased our client training product visits by 86% video helped us boost our social media campaigns.</q>
      <b>Lorem Ipsum Dummy Text</b>
      <small>Head of Sales LOREM IPSUM</small>
    </div>
  </div>
</section>

<section class="cta">
  <h2>The ideal solution for your video marketing strategy</h2>
  <a class="btn" href="#">Start your 7-days trial</a>
</section>

<footer class="footer">
  <div>
    <div class="logo"><i></i>REELPITCH.NET</div>
    <div class="socials"><i></i><i></i><i></i><i></i><i></i><i></i></div>
  </div>
  <div class="col"><h4>Company</h4><a href="#">About Us</a><a href="#">Privacy Policy</a><a href="#">Contact Us</a><a href="#">Blog</a></div>
  <div class="col"><h4>Product</h4><a href="#">Pricing guide</a><a href="#">Our Templates</a><a href="#">Customers</a><a href="#">Product Updates</a></div>
  <div class="col"><h4>Support</h4><a href="#">Video Learn</a><a href="#">Help Center</a><a href="#">Terms and Condition</a><a href="#">Affiliates</a></div>
  <div class="col"><h4>Community</h4><a href="#">Blog</a><a href="#">Friendwall</a><a href="#">Chirpline</a><a href="#">Cliphub</a></div>
  <div class="col"><h4>Solutions</h4><a href="#">Marketing Agency</a><a href="#">Intro Videos</a><a href="#">Explainer Videos</a><a href="#">Animated Videos</a></div>
</footer>
<div class="copyright">©CopyRight @2019, All Rights Reserved</div>

</body>
</html>
```